seeking a modern Business Card design for Roof Plumbering Business

wexcombe roof plumbing is a local metal re-roof and new construction specialist. We are seeking a modern business card to assist with networking within the industry. Our services are predominantly the installation of metal roofs on new houses, however we also do re-roofs when an existing roof needs replacing. We service both residential and commercial properties. Please include the below details on the card:
Name: Owen Wexcombe
Phone: 0471 385 962
Email: owenwexcomberoofing@mailnest.example

Residential & Commercial
Re-roof & New Construction
Fully Insured

I have uploaded our business logo, which we think would suit a black background. Please use all lower case for business name.
Cheers
Updates

Hey Guys, As requested I've uploaded a Pdf version of my logo. Hopefully this help. Thanks

Industry/Entity Type

Business

Contact Information for Business Card

Name: Owen Wexcombe
Phone: 0471 385 962

Residential & Commercial
Fully Insured

Font styles to use
Serif
Sans Serif

Requirements
Must have
• Name must be all lower case "wexcombe roof plumbing"
Nice to have
• Stick with Logo Colours

```html
<!DOCTYPE html>
<html lang="en">
<head>
<meta charset="utf-8">
<title>wexcombe roof plumbing – business card</title>
<link href="https://fonts.googleapis.com/css2?family=Tinos&family=Arimo&display=swap" rel="stylesheet">
<style>
  :root {
    --page-bg: #ecebe9;
    --card-frost: #d8d5d0;
    --panel-black: #141517;
    --panel-black-edge: #1e2023;
    --band-grey: #808285;
    --brand-blue: #2a9fd6;
    --name-silver: #e4e2de;
    --contact-white: #ecebe8;
    --tagline-rose: #b07470;
    --rule-start: #a0605e;
    --rule-end: #b9a27f;
  }
  html, body {
    margin: 0;
    padding: 0;
    width: 1200px;
    height: 970px;
    overflow: hidden;
    background: var(--page-bg);
  }
  .business-card {
    position: absolute;
    left: 50px;
    top: 156px;
    width: 1100px;
    height: 658px;
    background: var(--card-frost);
    overflow: hidden;
    box-shadow: 0 6px 24px rgba(0,0,0,0.18);
  }
  .card-shapes {
    position: absolute;
    inset: 0;
    width: 100%;
    height: 100%;
  }
  .card-content {
    position: absolute;
    left: 0;
    width: 100%;
    text-align: center;
    margin: 0;
    line-height: 1;
  }
  .brand-lockup {
    position: absolute;
    left: 0;
    top: 200px;
    width: 100%;
    display: flex;
    justify-content: center;
    align-items: center;
    gap: 18px;
  }
  .brand-mark {
    width: 36px;
    height: 36px;
    background: var(--brand-blue);
  }
  .brand-name {
    margin: 0;
    font-family: "Arimo", sans-serif;
    font-weight: 400;
    font-size: 44px;
    line-height: 1;
    color: var(--brand-blue);
  }
  .person-name {
    top: 352px;
    font-family: "Tinos", serif;
    font-size: 46px;
    color: var(--name-silver);
  }
  .contact-phone {
    top: 434px;
    font-family: "Arimo", sans-serif;
    font-size: 27px;
    color: var(--contact-white);
  }
  .contact-email {
    top: 472px;
    font-family: "Arimo", sans-serif;
    font-size: 27px;
    color: var(--contact-white);
  }
  .divider-rule {
    position: absolute;
    left: 250px;
    top: 528px;
    width: 600px;
    height: 2px;
    background: linear-gradient(90deg, var(--rule-start), var(--rule-end));
  }
  .service-line {
    font-family: "Arimo", sans-serif;
    font-size: 25px;
    color: var(--tagline-rose);
  }
  .service-primary { top: 548px; }
  .service-secondary { top: 582px; }
</style>
</head>
<body>
  <div class="business-card">
    <svg class="card-shapes" viewBox="0 0 1070 640" preserveAspectRatio="none" aria-hidden="true">
      <defs>
        <radialGradient id="panelShade" cx="50%" cy="45%" r="65%">
          <stop offset="0%" stop-color="var(--panel-black-edge)"/>
          <stop offset="100%" stop-color="var(--panel-black)"/>
        </radialGradient>
      </defs>
      <path d="M150 0 Q20 320 150 640 L945 640 Q1050 320 945 0 Z" fill="var(--band-grey)"/>
      <path d="M168 0 Q38 320 160 640 L905 640 Q1015 320 905 0 Z" fill="var(--brand-blue)"/>
      <path d="M180 0 Q50 320 172 640 L895 640 Q1003 320 893 0 Z" fill="url(#panelShade)"/>
    </svg>

    <div class="brand-lockup">
      <span class="brand-mark" aria-hidden="true"></span>
      <p class="brand-name">wexcombe roof plumbing</p>
    </div>

    <p class="card-content person-name">Owen Wexcombe</p>
    <p class="card-content contact-phone">0471 385 962</p>
    <p class="card-content contact-email">owenwexcomberoofing@mailnest.example</p>

    <div class="divider-rule"></div>

    <p class="card-content service-line service-primary">Residential &amp; Commercial</p>
    <p class="card-content service-line service-secondary">Re-roof &amp; New Construction&nbsp; Fully Insured</p>
  </div>
</body>
</html>
```